Business Card Design

We are starting up a new Family run Business mainly offering a Free House Clearance service. We also offer the following chargeable services which include a Removals Service, Delivery and Collection of Items sold or purchased on Bidloft, Swapcorner etc, including Motorcycles, Piano's, Furniture, Electrical appliances.
As there are a few Companies offering similar services we need to stand out and show what we do at a glance while appearing Professional and approachable
Updates

TidyNests

i  am liking some of the colours and designs so far but would like to see a few of our services listed as 1 or 2 have already done if this is possible and maybe some emphasis on the FREE House Clearance. thank you 
best regards
derek

Target Market(s)

Commercial and Domestic Tenants and Landlords aswell as Families looking for a friendly sympathetic clearance service after bereavement

Industry/Entity Type

Business

Contact Information for Business Card

TidyNests,
HouseClearance and Removals,
Brynmor Vale
CF47 2RL
Tel: 07831562904
Email: enquiries@tidynests.example

```html
<!DOCTYPE html>
<html lang="en">
<head>
<meta charset="utf-8">
<title>TidyNests – Business Card</title>
<link href="https://fonts.googleapis.com/css2?family=Open+Sans:wght@400;600;700&display=swap" rel="stylesheet">
<style>
  :root {
    --page: #ecebe8;
    --card-white: #ffffff;
    --brand-blue: #1b8fd0;
    --deep-blue: #0f6db3;
    --light-blue: #35b3e3;
    --ink: #3a3a3a;
    --ink-soft: #555555;
    --ink-strong: #222222;
  }
  * { margin: 0; padding: 0; box-sizing: border-box; }
  html, body {
    width: 1200px; height: 800px; overflow: hidden;
    background: var(--page);
    font-family: "Open Sans", Arial, sans-serif;
  }
  .card {
    position: absolute;
    top: 251px;
    width: 520px; height: 297px;
    border-radius: 16px;
    overflow: hidden;
    box-shadow: 0 6px 18px rgba(0,0,0,0.18);
  }

  /* ---------- back side ---------- */
  .card-back {
    left: 50px;
    background: linear-gradient(135deg, var(--light-blue) 0%, var(--brand-blue) 50%, var(--deep-blue) 100%);
    color: var(--card-white);
  }
  .card-back .brand-block {
    position: absolute;
    left: 0; right: 0; top: 108px;
    text-align: center;
  }
  .card-back .brand-name {
    font-size: 44px; font-weight: 400; letter-spacing: 0.5px; line-height: 1;
  }
  .card-back .brand-tagline {
    margin-top: 8px;
    font-size: 19px; font-weight: 700;
  }

  /* ---------- front side ---------- */
  .card-front {
    left: 630px;
    background: var(--card-white);
    color: var(--ink);
  }
  .front-brand {
    position: absolute; left: 30px; top: 52px;
  }
  .front-brand .brand-mark {
    display: inline-block; width: 14px; height: 14px;
    border-radius: 50%; background: var(--brand-blue);
    vertical-align: middle; margin-right: 8px;
  }
  .front-brand .brand-name {
    font-size: 36px; font-weight: 400; color: var(--ink);
    vertical-align: middle; line-height: 1;
  }
  .front-brand .brand-tagline {
    margin-top: 6px;
    font-size: 17px; font-weight: 400; color: var(--ink);
  }
  .service-list {
    position: absolute; left: 318px; top: 26px;
    list-style: none;
    font-size: 12.5px; line-height: 1.55; color: var(--ink-soft);
  }
  .service-list li::before {
    content: ""; display: inline-block;
    width: 6px; height: 6px; border-radius: 50%;
    background: var(--brand-blue);
    margin-right: 8px; vertical-align: middle;
  }
  .accent-arc {
    position: absolute; left: 0; top: 0;
    width: 520px; height: 297px;
  }
  .free-offer {
    position: absolute; left: 392px; right: 8px; top: 208px;
    text-align: center; white-space: nowrap;
    font-weight: 700; font-size: 14px; line-height: 1.4; color: var(--ink-strong);
  }
  .contact-person {
    position: absolute; left: 30px; top: 175px;
  }
  .contact-person .person-name {
    font-size: 18px; font-weight: 700; color: var(--brand-blue); letter-spacing: 0.3px;
  }
  .contact-person .person-role {
    font-size: 12px; font-weight: 600; color: var(--ink);
  }
  .contact-list {
    position: absolute; left: 30px; top: 222px;
    list-style: none;
    font-size: 12.5px; line-height: 1.55; color: var(--ink-soft);
  }
  .contact-list li { display: flex; align-items: center; gap: 8px; }
  .contact-icon { width: 13px; height: 13px; flex: none; }
</style>
</head>
<body>

  <section class="card card-back" aria-label="Card back">
    <div class="brand-block">
      <div class="brand-name">TidyNests</div>
      <div class="brand-tagline">HouseClearance and Removals</div>
    </div>
  </section>

  <section class="card card-front" aria-label="Card front">
    <svg class="accent-arc" viewBox="0 0 520 297" aria-hidden="true">
      <circle cx="700" cy="420" r="360" fill="none" stroke="#1b8fd0" stroke-width="16"/>
    </svg>

    <div class="front-brand">
      <span class="brand-mark"></span><span class="brand-name">TidyNests</span>
      <div class="brand-tagline">House Clearance and Removals</div>
    </div>

    <ul class="service-list">
      <li>Removals Service</li>
      <li>Delivery</li>
      <li>Collection</li>
    </ul>

    <div class="free-offer">FREE<br>House Clearance</div>

    <div class="contact-person">
      <div class="person-name">OWEN HARLOW</div>
      <div class="person-role">Director</div>
    </div>

    <ul class="contact-list">
      <li>
        <svg class="contact-icon" viewBox="0 0 14 14" aria-hidden="true">
          <circle cx="7" cy="7" r="7" fill="#1b8fd0"/>
          <rect x="4.5" y="3" width="5" height="8" rx="1" fill="#fff"/>
          <rect x="5.4" y="4" width="3.2" height="5" fill="#1b8fd0"/>
        </svg>
        <span>07831562904</span>
      </li>
      <li>
        <svg class="contact-icon" viewBox="0 0 14 14" aria-hidden="true">
          <circle cx="7" cy="7" r="7" fill="#1b8fd0"/>
          <rect x="3.5" y="4.5" width="7" height="5" fill="#fff"/>
          <path d="M3.5 4.5 L7 7.5 L10.5 4.5" fill="none" stroke="#1b8fd0" stroke-width="0.9"/>
        </svg>
        <span>enquiries@tidynests.example</span>
      </li>
      <li>
        <svg class="contact-icon" viewBox="0 0 14 14" aria-hidden="true">
          <circle cx="7" cy="7" r="7" fill="#1b8fd0"/>
          <path d="M7 11 C5 8.5 4.5 7.5 4.5 6.3 A2.5 2.5 0 0 1 9.5 6.3 C9.5 7.5 9 8.5 7 11 Z" fill="#fff"/>
          <circle cx="7" cy="6.2" r="0.9" fill="#1b8fd0"/>
        </svg>
        <span>Brynmor Vale CF47 2RL</span>
      </li>
    </ul>
  </section>

</body>
</html>
```